BRISKA sparkling water needs new artwork! Based in Southern California

"Briska" is a new sparkling water company based in Southern California that offers refreshing flavors (lime, cherry, & mango) with B vitamins and antioxidants.

We would like to see packaging designs for standard 12oz cans for each of the three flavors.
Our initial preference is to have individual artwork for each flavor.

Attached are examples of competitors' designs.
Updates

We are extending the deadline for the Thanksgiving Holiday. Thank you all for your contributions.

```html
<!DOCTYPE html>
<html lang="en">
<head>
<meta charset="utf-8">
<title>Briska Sparkling Water – Cherry Can Label</title>
<link rel="stylesheet" href="https://fonts.googleapis.com/css2?family=Big+Shoulders+Display:wght@500&family=Montserrat:wght@600;700&display=swap">
<style>
  :root {
    --plum: #6b1d5a;
    --berry: #a8285f;
    --rose: #c52a55;
    --cherry-red: #e21f2c;
    --ribbon-silver: #c8c8cb;
    --ink-plum: #5a1a4a;
    --white: #ffffff;
    --page: #ffffff;
  }
  * { box-sizing: border-box; margin: 0; padding: 0; }
  html, body {
    width: 1200px;
    height: 1200px;
    overflow: hidden;
    background: var(--page);
  }
  .canvas {
    position: relative;
    width: 1200px;
    height: 1200px;
  }
  .can-label {
    position: absolute;
    left: 300px;
    top: 90px;
    width: 600px;
    height: 1020px;
    background: linear-gradient(180deg,
      var(--plum) 0%,
      var(--berry) 35%,
      var(--rose) 60%,
      var(--cherry-red) 100%);
    overflow: hidden;
  }
  .size-ribbon {
    position: absolute;
    left: 262px;
    top: 0;
    width: 76px;
    height: 175px;
    background: var(--ribbon-silver);
    clip-path: polygon(0 0, 100% 0, 100% 100%, 50% 88%, 0 100%);
    display: flex;
    flex-direction: column;
    align-items: center;
    justify-content: flex-start;
    padding-top: 80px;
    font-family: "Montserrat", sans-serif;
    font-weight: 700;
    color: var(--ink-plum);
    line-height: 0.9;
  }
  .size-ribbon .size-number { font-size: 34px; }
  .size-ribbon .size-unit { font-size: 24px; }
  .fruit-art {
    position: absolute;
    left: 90px;
    top: 170px;
    width: 440px;
    height: 400px;
  }
  .brand-name {
    position: absolute;
    left: 0;
    width: 100%;
    top: 560px;
    text-align: center;
    font-family: "Big Shoulders Display", sans-serif;
    font-weight: 500;
    font-size: 215px;
    line-height: 1;
    letter-spacing: 2px;
    color: var(--white);
  }
  .descriptor {
    position: absolute;
    left: 0;
    width: 100%;
    top: 835px;
    text-align: center;
    font-family: "Montserrat", sans-serif;
    font-weight: 700;
    color: var(--white);
  }
  .descriptor .descriptor-small {
    font-size: 14px;
    letter-spacing: 0.5px;
  }
  .descriptor .descriptor-main {
    margin-top: 6px;
    font-size: 24px;
    letter-spacing: 1px;
  }
  .flavor-pill {
    position: absolute;
    left: 50%;
    top: 940px;
    transform: translateX(-50%);
    background: var(--white);
    color: var(--cherry-red);
    font-family: "Montserrat", sans-serif;
    font-weight: 700;
    font-size: 19px;
    padding: 5px 24px;
    border-radius: 20px;
  }
</style>
</head>
<body>
<main class="canvas">
  <section class="can-label">
    <div class="size-ribbon">
      <span class="size-number">12</span>
      <span class="size-unit">oz</span>
    </div>

    <svg class="fruit-art" role="img" aria-label="Watercolour illustration of a cluster of red cherries on green stems with leaves" viewBox="0 0 440 400">
      <defs>
        <radialGradient id="cherry-tone" cx="50%" cy="62%" r="55%">
          <stop offset="0%" stop-color="#e2283a" stop-opacity="0.9"/>
          <stop offset="60%" stop-color="#c42340" stop-opacity="0.45"/>
          <stop offset="100%" stop-color="#c42340" stop-opacity="0"/>
        </radialGradient>
      </defs>
      <rect width="440" height="400" fill="url(#cherry-tone)"/>
    </svg>

    <h1 class="brand-name">BRISKA</h1>

    <div class="descriptor">
      <p class="descriptor-small">NATURALLY FLAVORED</p>
      <p class="descriptor-main">SPARKLING WATER</p>
    </div>

    <div class="flavor-pill">CHERRY</div>
  </section>
</main>
</body>
</html>
```